Simply Sugar Bloom Buisness Card

I would like a Buisness card and matching letterhead for my small but personal hobby/buisness.
Something elegant, professional and pretty.
I mainly do wedding cakes in our small rural area. But also do occasion cakes, cupcakes, cookies and catering events.
I am thinking something subtle, vintage, scrolls, lace, damask, nothing too wow or out there. But open to any suggestions.

Industry/Entity Type

Catering

Contact Information for Business Card

Simply Sugar Bloom
abn: 41 503 917 248
Marnie Holloway
Brindlewood
t: 0491 352 806
e: sugarbloomcakes@pastrymail.example

Logo Text

Simply Sugar Bloom

Logo styles of interest
Wordmark Logo
Requirements
Must have
• Elegance and class
Should not have
• Should not have Hearts or Bows

```html
<!DOCTYPE html>
<html lang="en">
<head>
<meta charset="utf-8">
<title>Simply Sugar Bloom – Business Card</title>
<link rel="stylesheet" href="https://fonts.googleapis.com/css2?family=Alegreya:wght@400&family=Open+Sans:wght@400&display=swap">
<style>
  :root {
    --backdrop: #eceded;
    --plum: #8a1f55;
    --blush: #f9e6e7;
    --paper: #ffffff;
    --ink: #2b2b2b;
  }
  html, body {
    margin: 0;
    width: 1200px;
    height: 794px;
    overflow: hidden;
    background: var(--backdrop);
  }
  .card {
    position: absolute;
    left: 185px;
    top: 143px;
    width: 834px;
    height: 478px;
    background: linear-gradient(90deg, var(--paper) 0%, var(--paper) 55%, var(--blush) 100%);
    font-family: "Alegreya", Georgia, serif;
    font-variant-numeric: lining-nums;
  }
  .floral-band {
    position: absolute;
    left: 0;
    top: 0;
    width: 170px;
    height: 100%;
    background: var(--plum);
  }
  .wordmark {
    position: absolute;
    left: 238px;
    top: 78px;
    margin: 0;
    font-size: 57px;
    font-weight: 400;
    line-height: 1;
    color: var(--plum);
    white-space: nowrap;
  }
  .tagline {
    position: absolute;
    left: 237px;
    top: 168px;
    margin: 0;
    font-size: 30px;
    color: var(--plum);
    white-space: nowrap;
  }
  .abn {
    position: absolute;
    left: 245px;
    top: 220px;
    margin: 0;
    font-family: "Open Sans", Arial, sans-serif;
    font-size: 15px;
    letter-spacing: 0.5px;
    color: var(--ink);
  }
  .contact {
    position: absolute;
    left: 313px;
    top: 285px;
    color: var(--ink);
  }
  .contact-name {
    margin: 0 0 10px;
    font-size: 26px;
    white-space: nowrap;
  }
  .contact-line {
    display: flex;
    align-items: center;
    margin: 0 0 8px;
    font-size: 23px;
    letter-spacing: 0.5px;
    white-space: nowrap;
  }
  .contact-line svg {
    flex: none;
    margin-right: 16px;
    fill: var(--plum);
  }
  .contact-line .phone-icon {
    margin-right: 21px;
  }
</style>
</head>
<body>
  <section class="card">
    <div class="floral-band" role="img" aria-label="Decorative pattern of pale pink flowers and leaves on a plum ground"></div>

    <h1 class="wordmark">Simply Sugar Bloom</h1>
    <p class="tagline">Wedding Cake Baker</p>
    <p class="abn">ABN: 41 503 917 248</p>

    <div class="contact">
      <p class="contact-name">Marnie Holloway Brindlewood</p>
      <p class="contact-line">
        <svg class="phone-icon" width="22" height="22" viewBox="0 0 24 24" aria-hidden="true">
          <path d="M6.6 10.8a15.5 15.5 0 0 0 6.6 6.6l2.2-2.2c.3-.3.7-.4 1-.2 1.1.4 2.3.6 3.6.6.6 0 1 .4 1 1V20c0 .6-.4 1-1 1A17 17 0 0 1 3 4c0-.6.4-1 1-1h3.5c.6 0 1 .4 1 1 0 1.3.2 2.5.6 3.6.1.3 0 .7-.2 1z"/>
        </svg>
        0491 352 806
      </p>
      <p class="contact-line">
        <svg width="24" height="18" viewBox="0 0 24 18" aria-hidden="true">
          <path d="M1 1h22v16H1z M3 3v.4l9 6.4 9-6.4V3z M3 5.8V15h18V5.8l-9 6.4z" fill-rule="evenodd"/>
        </svg>
        sugarbloomcakes@pastrymail.example
      </p>
    </div>
  </section>
</body>
</html>
```